Brookvale Systems Yellow rose letterhead

I have a new logo for my company but in its current form it is too large to be used on letterhead or as a email signature. I need to have the designer use elements from the current logo and create something close to the original but more suited for smaller items.
Updates

I just uploaded a copy of our logo that does not have the weathered affect. Thanks

Industry/Entity Type

It Company

Requirements
Must have
• The design must maintain the visual effect of the current logo. It needs to include the yellow rose and the name of the company.
Nice to have
• It would be nice to maintain the stamp theme and incorporate my name, address, phone, email. etc.

```html
<!DOCTYPE html>
<html lang="en">
<head>
<meta charset="utf-8">
<title>Brookvale Systems Letterhead</title>
<link href="https://fonts.googleapis.com/css2?family=Poiret+One&display=swap" rel="stylesheet">
<style>
  :root {
    --paper: #ffffff;
    --ink: #4b3c35;
    --frame-light: #fbe9a0;
    --frame-gold: #f2cf57;
    --rose-yellow: #f7cf3a;
    --rose-edge: #3cb8c8;
  }
  html, body {
    margin: 0;
    padding: 0;
    overflow: hidden;
    background: var(--paper);
  }
  .letterhead {
    position: relative;
    width: 772px;
    height: 1200px;
    box-sizing: border-box;
    background: var(--paper);
    border: 5px solid var(--frame-gold);
    border-image: linear-gradient(90deg, var(--frame-light), var(--frame-gold) 50%, var(--frame-light)) 1;
    font-family: "Poiret One", sans-serif;
    color: var(--ink);
    overflow: hidden;
  }
  .brand-mark {
    position: absolute;
    left: 30px;
    top: 20px;
    width: 130px;
    height: 130px;
  }
  .brand-name {
    position: absolute;
    left: 198px;
    top: 30px;
    width: 506px;
    margin: 0;
    font-weight: 400;
    font-size: 60px;
    line-height: 72px;
    white-space: nowrap;
    letter-spacing: 0.5px;
    -webkit-text-stroke: 1.2px var(--ink);
  }
  .brand-rule {
    position: absolute;
    left: 203px;
    top: 110px;
    width: 498px;
    height: 2px;
    background: var(--ink);
  }
  .footer-rule {
    position: absolute;
    left: 16px;
    top: 1019px;
    width: 738px;
    height: 2px;
    background: var(--ink);
  }
  .contact {
    position: absolute;
    left: 18px;
    top: 1024px;
    margin: 0;
    padding: 0;
    list-style: none;
    font-size: 29px;
    line-height: 32.5px;
    letter-spacing: 1px;
    -webkit-text-stroke: 1.4px var(--ink);
    white-space: nowrap;
  }
</style>
</head>
<body>
  <main class="letterhead">
    <svg class="brand-mark" viewBox="0 0 130 130" role="img" aria-label="Brookvale Systems brand mark">
      <circle cx="65" cy="65" r="60" fill="var(--rose-yellow)"/>
    </svg>
    <h1 class="brand-name">Brookvale Systems</h1>
    <div class="brand-rule"></div>

    <div class="footer-rule"></div>
    <ul class="contact">
      <li class="contact-name">Dana Whitcomb, PhD</li>
      <li class="contact-street">418 NW Cedar Ridge Road, STE 1170</li>
      <li class="contact-city">Maple Hollow, TX 75512</li>
      <li class="contact-email">dana@brookvale-systems.com</li>
      <li class="contact-phone">1-800-555-0147</li>
    </ul>
  </main>
</body>
</html>
```